Criação de Papelaria Profissional para Vértice & Prisma
A empresa queria:
" Desenvolve, vende, implanta o Software e da suporte (Atendimento ao cliente). "

```html
<!DOCTYPE html>
<html lang="pt-BR">
<head>
<meta charset="UTF-8">
<title>Vértice &amp; Prisma — Papelaria</title>
<link href="https://fonts.googleapis.com/css2?family=Montserrat:wght@400;600;800&display=swap" rel="stylesheet">
<style>
  :root {
    --bg: #d9d9d9;
    --ink: #1a1a1a;
    --orange: #f08a1c;
    --paper: #ffffff;
    --muted: #bdbdbd;
    --ghost: #f1f1f1;
  }
  * { margin: 0; padding: 0; box-sizing: border-box; }
  html, body { width: 1200px; height: 1200px; overflow: hidden; }
  body {
    background: var(--bg);
    font-family: "Montserrat", Arial, sans-serif;
    position: relative;
  }
  .envelope {
    position: absolute; left: 90px; top: 250px;
    width: 480px; height: 680px;
    background: var(--ink);
    overflow: hidden;
  }
  .envelope__flap { position: absolute; left: 0; top: 0; width: 480px; height: 46px; }
  .envelope__band {
    position: absolute; left: 0; bottom: 0; width: 100%; height: 14px;
    background: var(--orange);
  }
  .envelope__rule {
    position: absolute; left: 0; bottom: 22px; width: 100%; height: 2px;
    background: var(--orange);
  }
  .brand {
    position: absolute; left: 0; width: 100%;
    display: flex; justify-content: center; align-items: center; gap: 12px;
  }
  .brand__dot {
    width: 30px; height: 30px; border-radius: 50%; background: var(--orange); flex: none;
  }
  .brand__text { display: flex; flex-direction: column; }
  .brand__name { font-weight: 800; font-size: 28px; letter-spacing: -0.5px; line-height: 1; }
  .brand__tag {
    font-weight: 600; font-size: 10px; letter-spacing: 5px; text-transform: uppercase;
    color: var(--orange); text-align: right; margin-top: 4px;
  }
  .envelope .brand { top: 120px; }
  .envelope .brand__name { color: var(--paper); }
  .contacts {
    position: absolute; left: 30px; right: 30px; bottom: 48px;
    display: grid; grid-template-columns: 1fr 1fr; gap: 8px 20px;
    color: var(--muted); font-size: 10px; line-height: 1.35;
  }
  .contact { display: flex; align-items: flex-start; gap: 7px; }
  .contact svg { flex: none; width: 12px; height: 12px; }
  .letterhead {
    position: absolute; left: 630px; top: 250px;
    width: 480px; height: 680px;
    background: var(--paper);
    overflow: hidden;
  }
  .letterhead__ghost {
    position: absolute; left: 70px; top: 260px;
    width: 340px; height: 340px; border-radius: 50%;
    background: var(--ghost);
  }
  .letterhead .brand { top: 300px; }
  .letterhead .brand__name { color: var(--ink); }
  .letterhead__rule {
    position: absolute; left: 0; bottom: 0; width: 100%; height: 10px;
    background: var(--orange);
  }
</style>
</head>
<body>
  <section class="envelope" aria-label="Envelope">
    <svg class="envelope__flap" viewBox="0 0 480 46" aria-hidden="true">
      <polygon points="0,0 480,0 480,46 430,14 50,14 0,46" fill="#f08a1c"/>
    </svg>
    <div class="brand">
      <span class="brand__dot"></span>
      <div class="brand__text">
        <span class="brand__name">Vértice &amp; Prisma</span>
        <span class="brand__tag">Software</span>
      </div>
    </div>
    <div class="contacts">
      <div class="contact">
        <svg viewBox="0 0 12 12"><circle cx="6" cy="6" r="6" fill="#f08a1c"/><path d="M4 3.2l1 1.4-.6.7a4 4 0 002.3 2.3l.7-.6 1.4 1-.5.9c-2.6-.2-4.9-2.5-5.1-5.1z" fill="#1a1a1a"/></svg>
        <span>(85) 3000-0000</span>
      </div>
      <div class="contact">
        <svg viewBox="0 0 12 12"><circle cx="6" cy="6" r="6" fill="#f08a1c"/><circle cx="6" cy="6" r="3" fill="none" stroke="#1a1a1a" stroke-width="1"/><path d="M3 6h6M6 3v6" stroke="#1a1a1a" stroke-width=".8"/></svg>
        <span>www.verticeprisma.com.br</span>
      </div>
      <div class="contact">
        <svg viewBox="0 0 12 12"><circle cx="6" cy="6" r="6" fill="#f08a1c"/><rect x="3" y="4" width="6" height="4" fill="none" stroke="#1a1a1a" stroke-width=".9"/><path d="M3 4l3 2.2L9 4" fill="none" stroke="#1a1a1a" stroke-width=".9"/></svg>
        <span>contato@verticeprisma.com.br</span>
      </div>
      <div class="contact">
        <svg viewBox="0 0 12 12"><circle cx="6" cy="6" r="6" fill="#f08a1c"/><path d="M6 9.5S3.6 6.8 3.6 5.1a2.4 2.4 0 014.8 0C8.4 6.8 6 9.5 6 9.5z" fill="#1a1a1a"/></svg>
        <span>Rua das Flores, 120 Centro<br>Fortaleza-CE, 60000-000</span>
      </div>
    </div>
    <div class="envelope__rule"></div>
    <div class="envelope__band"></div>
  </section>

  <section class="letterhead" aria-label="Papel timbrado">
    <div class="letterhead__ghost"></div>
    <div class="brand">
      <span class="brand__dot"></span>
      <div class="brand__text">
        <span class="brand__name">Vértice &amp; Prisma</span>
        <span class="brand__tag">Software</span>
      </div>
    </div>
    <div class="letterhead__rule"></div>
  </section>
</body>
</html>
```